Virtual Assistant/Online Marketing Business Card/Stationary

I need a professional but modern business card/stationary for my company in Dallas called Brivolo. Brivolo is a virtual assistant specializing in online marketing. I would like a unique design that stands out and makes my brand clear. Incorporating the logo is a must and have attached it to this brief.

Target Market(s)

small business owners & entrepreneurs, 35-65

Industry/Entity Type

Business

Contact Information for Business Card

Maren Tolk
marentolk@brivolo.biz
(555) 271-9064
brivolo.biz

Font styles to use
Sans Serif

Colors
f04a50
3176b5
9bcb3c

Requirements
Must have
• Colors that match the logo colors. Logo integration

```html
<!DOCTYPE html>
<html lang="en">
<head>
<meta charset="utf-8">
<title>Brivolo Business Card</title>
<link href="https://fonts.googleapis.com/css2?family=Open+Sans:ital,wght@0,400;0,600;0,700;1,400&display=swap" rel="stylesheet">
<style>
  :root {
    --backdrop: #a8a5a5;
    --paper: #ffffff;
    --ink: #33373b;
    --red: #c84a3c;
    --green: #7fbd45;
    --teal: #3aa3ab;
    --blue: #5b93c0;
    --muted: #3d4145;
  }
  * { margin: 0; padding: 0; box-sizing: border-box; }
  html, body { width: 1200px; height: 1200px; overflow: hidden; }
  body {
    background: var(--backdrop);
    font-family: "Open Sans", Arial, sans-serif;
    position: relative;
  }
  .card {
    position: absolute;
    width: 712px;
    height: 417px;
    background: var(--paper);
    overflow: hidden;
  }
  .card--front { left: 238px; top: 119px; }
  .card--back { left: 230px; top: 645px; }

  .brand-name {
    position: absolute;
    font-weight: 700;
    color: var(--ink);
    letter-spacing: -1px;
    line-height: 1;
  }
  .card--front .brand-name {
    left: 0; right: 0; top: 160px;
    text-align: center;
    font-size: 96px;
  }
  .card--back .brand-name {
    left: 58px; top: 140px;
    font-size: 88px;
  }

  .edge-band {
    position: absolute;
    left: 0; bottom: 0;
    width: 712px; height: 7px;
    background: linear-gradient(90deg, var(--green), var(--red), var(--teal), var(--ink), var(--blue));
  }

  .holder {
    position: absolute;
    right: 42px; top: 58px;
    text-align: right;
  }
  .holder__name { font-size: 27px; font-weight: 700; color: var(--ink); line-height: 1.2; }
  .holder__role { font-size: 15px; font-style: italic; color: var(--muted); margin-top: 2px; }

  .lower-band {
    position: absolute;
    left: 0; bottom: 0;
    width: 712px; height: 140px;
    background: linear-gradient(90deg, var(--teal) 0%, #2f5f66 30%, var(--ink) 60%);
  }

  .contact {
    position: absolute;
    right: 36px; top: 300px;
    list-style: none;
  }
  .contact__item {
    display: flex;
    justify-content: flex-end;
    align-items: center;
    gap: 16px;
    height: 26.5px;
    color: #ffffff;
    font-size: 16.5px;
  }
  .contact__icon { width: 17px; height: 17px; display: block; }
</style>
</head>
<body>

  <section class="card card--front">
    <div class="brand-name">Brivolo</div>
    <div class="edge-band" role="img" aria-label="Thin multicolour edge band in brand colours"></div>
  </section>

  <section class="card card--back">
    <div class="lower-band" role="img" aria-label="Decorative band in teal, red and charcoal brand tones"></div>

    <div class="brand-name">Brivolo</div>

    <div class="holder">
      <div class="holder__name">Maren Tolk</div>
      <div class="holder__role">Managing Director</div>
    </div>

    <ul class="contact">
      <li class="contact__item">
        <span>(555) 271-9064</span>
        <svg class="contact__icon" viewBox="0 0 20 20" aria-hidden="true">
          <path d="M2,7 C2,3 18,3 18,7 L15,8 L14,6 C11,5 9,5 6,6 L5,8 Z" fill="#fff"/>
          <path d="M6,9 L14,9 L17,17 L3,17 Z" fill="#fff"/>
          <circle cx="10" cy="13" r="2" fill="var(--ink)"/>
        </svg>
      </li>
      <li class="contact__item">
        <span>www.brivolo.biz</span>
        <svg class="contact__icon" viewBox="0 0 20 20" aria-hidden="true" fill="none" stroke="#fff" stroke-width="1.5">
          <circle cx="10" cy="10" r="8"/>
          <ellipse cx="10" cy="10" rx="3.5" ry="8"/>
          <line x1="2" y1="10" x2="18" y2="10"/>
          <line x1="3.5" y1="5.5" x2="16.5" y2="5.5"/>
          <line x1="3.5" y1="14.5" x2="16.5" y2="14.5"/>
        </svg>
      </li>
      <li class="contact__item">
        <span>marentolk@brivolo.biz</span>
        <svg class="contact__icon" viewBox="0 0 20 20" aria-hidden="true">
          <rect x="1" y="4" width="18" height="12" fill="#fff"/>
          <path d="M1,4 L10,11 L19,4" fill="none" stroke="var(--ink)" stroke-width="1.3"/>
          <path d="M1,16 L8,10 M19,16 L12,10" fill="none" stroke="var(--ink)" stroke-width="1.3"/>
        </svg>
      </li>
    </ul>
  </section>

</body>
</html>
```